Multifamily Investment Strategies

I need a pamphlet or booklet for multifamily commercial real estate investment.

The specific investment vehicle is affordable multifamily apartments. I have uploaded a 5 page pdf detailing my investment strategy.

The target audience for this pamphlet are investors, commercial brokers, and commercial bankers.

I am looking for modern, clean design that is striking and professional but also eye catching.
Updates

I made a few changes to the brief and also corrected two errors.

Target Market(s)

Commercial Real Estate Investors, Brokers, and Bankers

Industry/Entity Type

Real Estate

Font styles to use
Serif

Colors

Designer to choose colors to be used in the design.

Requirements
Must have
• Graphics of or related to apartment buildings.
• My headshot seen on the last page of the pdf
Nice to have
• Imagery related to investment and profits.
Should not have
• The image of an apartment building on the first page of the pdf is just an example. Please don’t use this image.

```html
<!DOCTYPE html>
<html lang="en">
<head>
<meta charset="utf-8">
<title>Multifamily Cashflow Investment Strategy – Page 3</title>
<link href="https://fonts.googleapis.com/css2?family=Source+Sans+3:wght@400;600&family=Arimo&display=swap" rel="stylesheet">
<style>
  :root {
    --accent: #e0885a;
    --ink: #1a1a1a;
    --muted: #555555;
    --panel: #f4f4f4;
    --page: #ffffff;
  }
  * { margin: 0; padding: 0; box-sizing: border-box; }
  html, body { width: 927px; height: 1200px; overflow: hidden; background: var(--page); }
  .page { position: relative; width: 927px; height: 1200px; font-family: "Source Sans 3", sans-serif; color: var(--ink); }
  .running-head { position: absolute; top: 53px; right: 92px; font-family: "Arimo", sans-serif; font-size: 14.5px; letter-spacing: 0.2px; color: var(--ink); }
  .running-head .accent { color: var(--accent); }
  .content-panel { position: absolute; left: 92px; top: 81px; width: 744px; height: 1038px; background: var(--panel); }
  .block { position: absolute; left: 152px; width: 650px; font-size: 13.6px; line-height: 24px; }
  .block.tight { line-height: 21.5px; }
  .label { color: var(--accent); font-weight: 600; }
  .section-title { position: absolute; left: 124px; font-size: 18.5px; font-weight: 600; }
  .bullets { position: absolute; left: 162px; width: 640px; font-size: 13.6px; line-height: 21.5px; list-style: none; }
  .bullets li { position: relative; padding-left: 16px; }
  .bullets li::before { content: ""; position: absolute; left: 2px; top: 8px; width: 5px; height: 5px; border-radius: 50%; background: var(--accent); }
  .bullets.spaced { line-height: 24px; }
  .bullets.spaced li::before { top: 7px; }
  .footer-name { position: absolute; left: 92px; top: 1139px; font-family: "Arimo", sans-serif; font-size: 14px; color: var(--muted); }
  .page-number { position: absolute; right: 92px; top: 1139px; font-family: "Arimo", sans-serif; font-size: 14px; color: var(--accent); }
</style>
</head>
<body>
<div class="page">
  <div class="running-head">MULTIFAMILY CASHFLOW <span class="accent">INVESTMENT STRATEGY</span></div>
  <div class="content-panel"></div>

  <p class="block" style="top:164px;"><span class="label">Property Class</span> - B and C class properties in A and B neighborhoods - Prefer 1980’s or newer.</p>
  <ul class="bullets" style="top:198px;">
    <li>These properties tend to house blue collar workers; don’t compete with new(er) construction; and don’t share the same challenges as C and D properties in C and D neighborhoods, which can encounter issues with crime, major disrepair, and increased vulnerability to economic downturns.</li>
  </ul>

  <p class="block" style="top:279px;"><span class="label">Market Analysis</span> - Target emerging markets with population and job growth; low to median cost of housing which allows rent growth (e.g., Columbus, Oklahoma, Atlanta, Dallas, Phoenix); median income of ~$35k/ yr; and landlord and business friendly rules and regulations (e.g., Ohio, Texas, Florida, Oklahoma, Colorado)</p>

  <p class="block" style="top:368px;"><span class="label">Scale</span> - 60+ units to support effective, third-party professional management. Additionally, targeting 60+ units will increase the likelihood of stability by creating a buffer against tenant turnover and other unplanned expenses.</p>

  <p class="block" style="top:456px;"><span class="label">Cash flow</span> - The property must generate cash flow from day one, before value add strategies are deployed.</p>
  <p class="block" style="top:493px;">Buy on <span class="label">actual numbers</span> instead of on pro forma analysis, which project or estimate financial return</p>

  <h2 class="section-title" style="top:557px;">2. Finance Right</h2>
  <p class="block" style="top:601px;"><span class="label">Longterm debt</span> - with long terms and amortization periods.</p>
  <p class="block tight" style="top:629px;"><span class="label">Non-recourse if possible.</span> e.g ., Keystone Housing Finance, Harborline Mortgage, CMBS. There is an extremely low foreclosure rate for Keystone and Harborline underwritten properties (1%-2%).</p>
  <p class="block" style="top:677px;"><span class="label">No prepayment penalty.</span></p>
  <p class="block" style="top:704px;"><span class="label">No due on sale clause.</span></p>

  <h2 class="section-title" style="top:763px;">2. Manage Right</h2>
  <p class="block" style="top:806px;"><span class="label">Third-Party Management</span> with experience in this specific class of multifamily real estate.</p>
  <ul class="bullets spaced" style="top:836px;">
    <li>Sizable but not too large that our property gets lost.</li>
    <li>Only in property management, not acquisition or development so that there is no conflict of interest.</li>
  </ul>
  <p class="block" style="top:891px; left:150px;"><span class="label">Use of Sole Purpose Entity Structures,</span> e.g., LLC’s for asset protection.</p>
  <p class="block" style="top:919px; left:150px;"><span class="label">Optimization</span> through use of systems.</p>
  <p class="block tight" style="top:947px; left:150px;"><span class="label">Tenant satisfaction</span> - Ensure great customer service to the tenant, e.g., 24 hour response to maintenance requests, cleanliness, and security. Happy tenants who feel heard and cared for, don’t leave, which limits tenant turnover, and lowers expenses.</p>
  <p class="block" style="top:1015px; left:150px;"><span class="label">Increase the “curb appeal”</span> - Freshened exterior with modern paint schemes, landscaping, and new signage. Rebranding with a name change, webpage, etc.</p>

  <div class="footer-name">Marisa Caldwell, Real Estate Investor.</div>
  <div class="page-number">3</div>
</div>
</body>
</html>
```